Smack you in the face - Landing page for Residential Electrical Repairs (Searchly Ads)

I need an effective landing page for Searchly ads. The ads will target residential electrical repairs. Lighting Outages, Power Outages, Breakers Tripping, Outlets Not Working. I need a strong call to action to Call Us Now! Forms don't work well for us so we only need one form as a last option at the bottom of the page. We only work on homes. the website is https://www.keystone-wiring.com/
email is : support@keystone-wiring.com
Phone 864-555-0172

**This is about one focused service. Electrical Repairs - That includes Partial Power Outages, Outlets Not Working, Tripped Breakers, Electrical Panel repairs, and Fusebox Repairs. The area served will only be Greenville, SC. VIMO is the platform

Target Market(s)

Homeonwers in need of electrical repair

Industry/Entity Type

Residential Electricians

Coding

Coded - Design and coding required

Requirements
Must have
• Strong to action for phone calls, this landing page must grab action fast.
Nice to have
• Social proof with existing 5 start reviews for Searchly, Rateo, TFC, and Friendhub
Should not have
• Should not be form based. I do not like the site's current them, please don't copy it. Make your own.

```html
<!DOCTYPE html>
<html lang="en">
<head>
<meta charset="utf-8">
<title>Keystone Wiring – Home Electrical Repairs in Greenville, SC</title>
<link rel="stylesheet" href="https://fonts.googleapis.com/css2?family=Poppins:wght@400;500;600;700;800;900&display=swap">
<style>
:root{
  --blue:#1e8fc7;
  --blue-dark:#12618f;
  --orange:#f26a1b;
  --ink:#1b1b1b;
  --muted:#555;
  --white:#fff;
  --night:#05080d;
  --pale:#eef2f6;
  --star:#f5a100;
}
*{margin:0;padding:0;box-sizing:border-box}
html,body{width:1200px;height:4213px;overflow:hidden}
body{position:relative;font-family:'Poppins',sans-serif;color:var(--ink);background:var(--white)}
.abs{position:absolute}
.btn{position:absolute;display:flex;align-items:center;justify-content:center;color:var(--white);font-weight:700;font-size:15px;border-radius:8px 8px 8px 0;text-transform:uppercase;white-space:nowrap}
.btn-orange{background:var(--orange)}
.btn-blue{background:var(--blue)}

/* header */
.topline{top:0;left:0;width:1200px;height:4px;background:var(--blue)}
.brand{display:flex;align-items:center;gap:10px;font-weight:800;font-size:28px;letter-spacing:1px;color:var(--ink);white-space:nowrap}
.brand-dot{width:22px;height:22px;border-radius:50%;background:var(--orange)}
.header-brand{left:110px;top:55px}
.nav{font-size:15px;font-weight:500;color:#333}
.nav a{position:absolute;white-space:nowrap;color:inherit;text-decoration:none}

/* hero */
.hero-art{top:148px;left:0}
.hero-title{left:113px;top:296px;color:var(--white);font-weight:800;font-size:55px;line-height:73px;text-transform:uppercase;white-space:nowrap}
.hero-title span{color:var(--orange)}
.hero-text{left:113px;top:528px;width:620px;color:var(--white);font-size:17px;line-height:37.5px;font-weight:500}

/* services */
.section-title{width:1200px;left:0;text-align:center;font-weight:800;font-size:43px;text-transform:uppercase}
.services-intro{left:160px;top:1066px;width:880px;text-align:center;font-size:13.5px;line-height:29px;color:var(--muted)}
.card{top:1190px;width:296px;height:465px;background:var(--white);border-radius:0 0 150px 150px;box-shadow:0 8px 22px rgba(0,0,0,.1)}
.card-img{position:absolute;left:11px;top:10px;width:274px;height:208px}
.card h3{position:absolute;top:248px;width:100%;text-align:center;font-size:17.5px;font-weight:600}
.card p{position:absolute;top:286px;left:14px;width:268px;text-align:center;font-size:11px;line-height:24px;color:var(--muted)}
.card svg.arrow{position:absolute;top:414px;left:136px}

/* reviews */
.reviews-bg{top:1850px;left:0}
.review{top:2150px;width:478px;height:343px;background:rgba(255,255,255,.88);box-shadow:0 6px 20px rgba(0,0,0,.06)}
.review .quote{position:absolute;left:38px;top:28px;font-size:56px;font-weight:900;color:var(--orange);line-height:56px;letter-spacing:-4px}
.review p{position:absolute;left:38px;top:80px;width:405px;font-size:13.5px;line-height:29px;color:#555}
.review .stars{position:absolute;left:38px;top:272px;color:var(--star);font-size:15px;letter-spacing:1px}
.review .who{position:absolute;left:38px;top:295px;font-weight:600;font-size:16px}
.review .src{position:absolute;right:45px;top:282px;width:34px;height:34px;border-radius:50%;border:5px solid var(--blue)}
.dots{top:2532px;left:552px;display:flex;gap:6px}
.dots i{display:block;width:14px;height:4px;background:#666}
.dots i.on{width:28px;background:var(--orange)}
.badge{top:2593px;width:160px;height:90px;background:var(--white);box-shadow:0 4px 14px rgba(0,0,0,.08);display:flex;align-items:center;justify-content:center}
.badge span{display:block;width:90px;height:34px;border-radius:6px}

/* about */
.about-photo{left:121px;top:2864px;width:474px;height:474px;border-radius:50%;border:6px solid var(--white);box-shadow:0 6px 24px rgba(0,0,0,.15);background:radial-gradient(circle at 50% 30%,#6d8fc2,#2b3c5c 55%,#1a2233)}
.about-title{left:643px;top:2910px;font-size:43px;font-weight:800;text-transform:uppercase}
.about-text{left:643px;top:2973px;width:450px;font-size:13.5px;line-height:29px;color:var(--muted)}

/* footer & contact */
.footer-art{top:3680px;left:0}
.contact{left:111px;top:3460px;width:978px;height:366px;background:var(--blue);border-radius:0 0 40px 0;box-shadow:0 10px 30px rgba(0,0,0,.2)}
.contact h2{position:absolute;top:38px;width:100%;text-align:center;color:var(--white);font-weight:800;font-size:42px}
.contact p{position:absolute;top:108px;left:80px;width:818px;text-align:center;color:var(--white);font-size:12px;line-height:26px}
.field{position:absolute;width:219px;height:48px;border:1px solid rgba(255,255,255,.8);color:var(--white);font-size:12.5px;padding-left:24px;display:flex;align-items:center}
.submit{position:absolute;width:219px;height:48px;background:var(--white);color:var(--orange);font-weight:700;font-size:15px;display:flex;align-items:center;justify-content:center;text-transform:uppercase}
.footer-brand{left:0;width:1200px;top:3935px;display:flex;justify-content:center}
.footer-brand .brand{color:var(--white);font-size:34px}
.footer-nav{top:4052px;color:var(--white);font-size:15.5px;white-space:nowrap}
.footer-info{top:4100px;color:var(--white);font-size:13px;display:flex;align-items:center;gap:10px;white-space:nowrap}
.social{top:4142px;left:562px;display:flex;gap:14px}
.social i{display:block;width:14px;height:14px;background:var(--white);border-radius:2px}
.copy{top:4172px;width:1200px;left:0;text-align:center;color:var(--white);font-size:11.5px}
</style>
</head>
<body>

<!-- header -->
<div class="abs topline"></div>
<div class="abs brand header-brand"><span class="brand-dot"></span>KEYSTONE WIRING</div>
<div class="btn btn-blue" style="left:783px;top:36px;width:145px;height:40px;">Call Us Now</div>
<div class="btn btn-orange" style="left:933px;top:36px;width:155px;height:40px;">864-555-0172</div>
<nav class="abs nav" style="left:0;top:93px;">
  <a style="left:405px">Home</a>
  <a style="left:509px">About Us</a>
  <a style="left:635px">Services</a>
  <a style="left:757px">Employment</a>
  <a style="left:912px">Blog</a>
  <a style="left:1003px">Contact Us</a>
</nav>

<!-- hero -->
<svg class="abs hero-art" width="1200" height="760" viewBox="0 0 1200 760">
  <defs>
    <linearGradient id="heroPhoto" x1="0" y1="0" x2="1" y2="0.6">
      <stop offset="0" stop-color="#1d2c3b"/>
      <stop offset=".55" stop-color="#2d4156"/>
      <stop offset="1" stop-color="#4a6a86"/>
    </linearGradient>
    <linearGradient id="heroBand" x1="0" y1="0" x2="1" y2="0">
      <stop offset="0" stop-color="#0f5d8f"/>
      <stop offset="1" stop-color="#1e8fc7"/>
    </linearGradient>
  </defs>
  <path d="M0 0H1200V500C1020 690 760 760 520 752C300 745 110 660 0 575Z" fill="url(#heroBand)"/>
  <path d="M0 0H1200V508C1010 660 760 720 520 712C300 705 110 640 0 560Z" fill="url(#heroPhoto)" role="img" aria-label="Electrician carrying a toolbox"/>
</svg>
<h1 class="abs hero-title">Welcome to<br>Keystone <span>Wiring</span><br>Service</h1>
<p class="abs hero-text">At Keystone Wiring, your home's electrical emergency is our urgency. Licensed electricians for same-day home repairs in Greenville, SC. Call us now for fast help.</p>
<div class="btn btn-orange" style="left:113px;top:660px;width:146px;height:42px;">Call Now</div>

<!-- services -->
<h2 class="abs section-title" style="top:988px;">Our Services</h2>
<p class="abs services-intro">When it comes to your home, the electrical system is a critical component that powers your day-to-day life. Understanding this, Keystone Wiring is committed to fast, reliable electrical repairs for Greenville homeowners, all tailored to keep your family safe and your home running.</p>

<div class="abs card" style="left:125px;">
  <div class="card-img" role="img" aria-label="Person checking a fuse box by candlelight" style="background:linear-gradient(135deg,#3a2414,#8a5a2c 55%,#2a1a10)"></div>
  <h3>Lighting Outages</h3>
  <p>Dislike men who are so beguiled and demoralized by the charms of pleasure of the moment, so blinded by desire, that they cannot foresee the pain and trouble that are bound to ensue; and equal blame</p>
  <svg class="arrow" width="24" height="12" viewBox="0 0 24 12"><path d="M0 6H21M16 1L22 6L16 11" stroke="#1e8fc7" stroke-width="2.2" fill="none"/></svg>
</div>
<div class="abs card" style="left:450px;">
  <div class="card-img" role="img" aria-label="Lightning storm over power lines" style="background:linear-gradient(180deg,#2c2450,#6a5a92 60%,#3a2e55)"></div>
  <h3>Power Outages</h3>
  <p>Dislike men who are so beguiled and demoralized by the charms of pleasure of the moment, so blinded by desire, that they cannot foresee the pain and trouble that are bound to ensue; and equal blame</p>
  <svg class="arrow" width="24" height="12" viewBox="0 0 24 12"><path d="M0 6H21M16 1L22 6L16 11" stroke="#1e8fc7" stroke-width="2.2" fill="none"/></svg>
</div>
<div class="abs card" style="left:775px;">
  <div class="card-img" role="img" aria-label="Electrician working on a breaker panel" style="background:linear-gradient(135deg,#c8562a,#7f98b8 50%,#2a57a8)"></div>
  <h3>Breakers Tripping</h3>
  <p>Dislike men who are so beguiled and demoralized by the charms of pleasure of the moment, so blinded by desire, that they cannot foresee the pain and trouble that are bound to ensue; and equal blame</p>
  <svg class="arrow" width="24" height="12" viewBox="0 0 24 12"><path d="M0 6H21M16 1L22 6L16 11" stroke="#1e8fc7" stroke-width="2.2" fill="none"/></svg>
</div>
<div class="btn btn-blue" style="left:461px;top:1694px;width:137px;height:40px;">View More</div>
<div class="btn btn-orange" style="left:610px;top:1694px;width:146px;height:40px;">Call Now</div>

<!-- reviews -->
<svg class="abs reviews-bg" width="1200" height="890" viewBox="0 0 1200 890">
  <defs>
    <linearGradient id="cityTone" x1="0" y1="0" x2="0" y2="1">
      <stop offset="0" stop-color="#f4f7fa"/>
      <stop offset="1" stop-color="#e3e8ee"/>
    </linearGradient>
  </defs>
  <path d="M0 220C200 70 460 0 640 0C880 0 1100 80 1200 150V887H0Z" fill="url(#cityTone)" role="img" aria-label="Faded city skyline"/>
  <path d="M0 260C200 80 460 5 640 5C900 5 1130 90 1200 160V230C1120 140 980 110 900 110C1080 200 1140 360 1120 520C1100 660 960 780 800 800L780 780C900 740 1010 650 1040 520C1080 330 930 150 640 100C400 70 150 160 0 300Z" fill="#1e8fc7"/>
</svg>
<h2 class="abs section-title" style="top:2045px;">Our Happy Customers</h2>

<div class="abs review" style="left:105px;">
  <div class="quote">“”</div>
  <p>Searched to find an electrician and Theo from Upland electric responded. He was very friendly, professional and showed interest in my dilemma. He made it easy to talk to and help me understand the urgency of my situation. He not only solved the issue but made me aware that I need to change my panel in the near future to remain safe.</p>
  <div class="stars">★★★★★</div>
  <div class="who">Dana Ellis</div>
  <span class="src"></span>
</div>
<div class="abs review" style="left:617px;">
  <div class="quote">“”</div>
  <p>Theo was wonderful and immediately identified what was tripping an electrical breaker box out by our pool. He then installed an electrical outlet for me that I requested in the attic; both jobs done very well in about an hours time. Thank you, Theo! Will definitely utilize his expertise in future. Wonderful electrician.</p>
  <div class="stars">★★★★★</div>
  <div class="who">Karen Poole</div>
  <span class="src"></span>
</div>
<div class="abs dots"><i class="on"></i><i></i><i></i><i></i></div>

<div class="abs badge" style="left:229px;" role="img" aria-label="Searchly reviews badge"><span style="background:#4a86e8"></span></div>
<div class="abs badge" style="left:422px;" role="img" aria-label="Rateo reviews badge"><span style="background:#d32323"></span></div>
<div class="abs badge" style="left:617px;" role="img" aria-label="TFC accredited badge"><span style="background:#1d5a8a"></span></div>
<div class="abs badge" style="left:813px;" role="img" aria-label="Friendhub reviews badge"><span style="background:#3b5998"></span></div>

<!-- about -->
<div class="abs about-photo" role="img" aria-label="Team and families gathered outdoors at night"></div>
<h2 class="abs about-title">About Us</h2>
<p class="abs about-text">Initiated by Evan Marsh in 2015 under the banner of Upland Electric Co, our journey began in Greenville, SC. Over the years, we've grown our local team and are now proudly serving Greenville homeowners as Keystone Wiring LLC. When an electrical issue arises in your home, you need swift and reliable solutions. That's precisely what we provide. We specialize in same-day repairs for residential customers, ensuring that your home remains a safe and comfortable space.</p>
<div class="btn btn-orange" style="left:643px;top:3231px;width:147px;height:42px;">Read More</div>

<!-- footer background -->
<svg class="abs footer-art" width="1200" height="533" viewBox="0 0 1200 533">
  <path d="M0 120C120 60 260 40 400 60C600 90 820 30 1000 0C1100 -10 1170 10 1200 20V533H0Z" fill="#0b1e33"/>
  <path d="M0 200C160 120 380 120 560 150C760 185 980 130 1200 80V533H0Z" fill="var(--night)"/>
</svg>

<!-- contact -->
<section class="abs contact">
  <h2>GET IN TOUCH WITH US</h2>
  <p>Our commitment to excellence is reflected in our online reputation. Our values aren't just words; they are reflected in every job we undertake and every relationship we build. Whether you're a Greenville homeowner facing an outage, a dead outlet or a tripping breaker, we're here for you. Call 864-555-0172 or reach out to Keystone Wiring today.</p>
  <div class="field" style="left:131px;top:208px;">First Name</div>
  <div class="field" style="left:379px;top:208px;">Last Name</div>
  <div class="field" style="left:628px;top:208px;">Contact Number</div>
  <div class="field" style="left:131px;top:270px;">Email Address</div>
  <div class="field" style="left:379px;top:270px;">Your Message</div>
  <div class="submit" style="left:628px;top:270px;">Submit Here</div>
</section>

<!-- footer -->
<div class="abs footer-brand"><div class="brand"><span class="brand-dot"></span>KEYSTONE WIRING</div></div>
<span class="abs footer-nav" style="left:258px;">Home</span>
<span class="abs footer-nav" style="left:361px;">About Us</span>
<span class="abs footer-nav" style="left:488px;">Services</span>
<span class="abs footer-nav" style="left:609px;">Employment</span>
<span class="abs footer-nav" style="left:765px;">Blog</span>
<span class="abs footer-nav" style="left:855px;">Contact Us</span>
<div class="abs footer-info" style="left:342px;">
  <svg width="12" height="16" viewBox="0 0 12 16"><path d="M6 0C2.7 0 0 2.6 0 5.8 0 10 6 16 6 16S12 10 12 5.8C12 2.6 9.3 0 6 0ZM6 8.2A2.3 2.3 0 1 1 6 3.6 2.3 2.3 0 0 1 6 8.2Z" fill="#fff"/></svg>
  120 Maple Ridge Rd, STE 4, Greenville, SC 29607
</div>
<div class="abs footer-info" style="left:728px;">
  <svg width="14" height="14" viewBox="0 0 14 14"><path d="M3 0L5.2 3.2 3.8 5C4.7 7 6.9 9.3 9 10.2L10.8 8.8 14 11 12.6 14C6 13.6 0.4 8 0 1.4Z" fill="#fff"/></svg>
  864-555-0172
</div>
<div class="abs social"><i></i><i></i><i></i></div>
<div class="abs copy">© Copyright 2023 Keystone Wiring Service | All rights reserved</div>

</body>
</html>
```